Business Card Design for Vantor Gear

We want to have a business card design for our company.
Company website: www.vantorgear-example.com.au
We looking for something cool, funky, and impressive, yet elegant.
Below are the contents that should be displayed on the card:
Front:
Name: Mark Dellow
Title: Sales & Purchasing
Company Name: Vantor Gear Pty Ltd
Phone: 02 5550 1473
Mobile: 0400 555 019
Email: mark@vantorgear-example.com.au
Website: www.vantorgear-example.com.au
Address: 17 Brackley St
Lidcombe, NSW 2141
Back:
We buy sell new used Norvex and network equipment
• Huge Savings - save up to 95% off list prices
• Highest Reliability
• Comprehensive Warranty
• Fast delivery
• Large range of hardware in stock
Our logo can be downloaded at: www.vantorgear-example.com.au/logo.zip

```html
<!DOCTYPE html>
<html lang="en">
<head>
<meta charset="utf-8">
<title>Vantor Gear – Business Card</title>
<link rel="stylesheet" href="https://fonts.googleapis.com/css2?family=Source+Sans+3:wght@400;600;700&display=swap">
<style>
  :root {
    --stage: #ece9e4;
    --card: #ffffff;
    --card-edge: #d6d2cc;
    --brand-blue: #2b6fd6;
    --navy: #27318a;
    --ink: #3a3a3a;
    --ink-soft: #555555;
    --accent-warm: #f7a35c;
    --accent-pink: #f2868f;
  }
  * { box-sizing: border-box; margin: 0; padding: 0; }
  html, body {
    width: 1200px; height: 407px; overflow: hidden;
    background: var(--stage);
    font-family: "Source Sans 3", Arial, sans-serif;
  }
  .stage { position: relative; width: 1200px; height: 407px; }
  .card {
    position: absolute; top: 54px; width: 508px; height: 290px;
    background: var(--card);
    border: 1px solid var(--card-edge);
    box-shadow: 0 2px 6px rgba(0,0,0,.18);
    overflow: hidden;
  }
  .card--front { left: 66px; }
  .card--back { left: 622px; }

  /* front */
  .brand { position: absolute; left: 19px; top: 16px; display: flex; align-items: center; }
  .brand__dot {
    width: 70px; height: 70px; border-radius: 50%;
    background: radial-gradient(circle at 40% 35%, var(--accent-warm), var(--accent-pink));
  }
  .brand__text { margin-left: 22px; }
  .brand__name { font-size: 33px; font-weight: 600; color: var(--brand-blue); line-height: 1; }
  .brand__tagline {
    margin-top: 6px; font-size: 7.5px; letter-spacing: 3.6px; color: var(--navy);
    text-transform: uppercase;
  }
  .decor-circle {
    position: absolute; left: 276px; top: 19px; width: 245px; height: 245px; border-radius: 50%;
    background: radial-gradient(circle at 55% 60%, #fde3c2 0%, #f9b7b2 55%, #f29a9f 100%);
    opacity: .85;
  }
  .person { position: absolute; left: 22px; top: 116px; }
  .person__name { font-size: 16.5px; font-weight: 700; color: var(--ink); }
  .person__title { font-size: 13px; font-weight: 400; color: var(--ink-soft); }
  .company { position: absolute; left: 22px; top: 156px; font-size: 13px; line-height: 20px; color: var(--ink-soft); }
  .company__name { font-weight: 700; color: var(--navy); }
  .contacts { position: absolute; left: 22px; top: 210px; list-style: none; font-size: 12.5px; color: var(--ink-soft); }
  .contacts li { display: flex; align-items: center; height: 18.5px; }
  .contacts svg { width: 10px; height: 10px; margin-right: 6px; fill: #444; }

  /* back */
  .headline { position: absolute; left: 21px; top: 62px; font-size: 16.5px; font-weight: 700; color: var(--navy); }
  .benefits { position: absolute; left: 21px; top: 108px; list-style: none; font-size: 16.5px; color: var(--ink); }
  .benefits li { height: 33.5px; }
  .benefits li::before { content: "• "; }
  .badge-circle {
    position: absolute; left: 372px; top: 143px; width: 114px; height: 114px; border-radius: 50%;
    background: radial-gradient(circle at 40% 35%, var(--accent-warm), var(--accent-pink));
  }
</style>
</head>
<body>
<main class="stage">
  <section class="card card--front" aria-label="Card front">
    <div class="decor-circle" aria-hidden="true"></div>
    <div class="brand">
      <div class="brand__dot" aria-hidden="true"></div>
      <div class="brand__text">
        <div class="brand__name">Vantor Gear</div>
        <div class="brand__tagline">Networking Equipment</div>
      </div>
    </div>
    <p class="person"><span class="person__name">Mark Dellow ,</span> <span class="person__title">Sales &amp; Purchasing</span></p>
    <p class="company"><span class="company__name">Vantor Gear Pty Ltd</span><br>17 Brackley St, Lidcombe, NSW 2141</p>
    <ul class="contacts">
      <li><svg viewBox="0 0 10 10"><path d="M2 0.5 L3.6 2.4 L2.8 3.6 Q4 6 6.4 7.2 L7.6 6.4 L9.5 8 L8.4 9.5 Q1 8.5 0.5 1.6 Z"/></svg>02 5550 1473</li>
      <li><svg viewBox="0 0 10 10"><path d="M2.5 0 H7.5 V10 H2.5 Z M3.3 1 V7.5 H6.7 V1 Z"/></svg>0400 555 019</li>
      <li><svg viewBox="0 0 10 10"><path d="M0 2 H10 V8.5 H0 Z M0.8 2.6 L5 5.6 L9.2 2.6 Z"/></svg>mark@vantorgear-example.com.au</li>
      <li><svg viewBox="0 0 10 10"><circle cx="5" cy="5" r="4.6"/></svg>www.vantorgear-example.com.au</li>
    </ul>
  </section>

  <section class="card card--back" aria-label="Card back">
    <h2 class="headline">We buy sell new used Norvex and network equipment</h2>
    <ul class="benefits">
      <li>Huge Savings - save up to 95% off list prices</li>
      <li>Highest Reliability</li>
      <li>Comprehensive Warranty</li>
      <li>Fast delivery</li>
      <li>Large range of hardware in stock</li>
    </ul>
    <div class="badge-circle" aria-hidden="true"></div>
  </section>
</main>
</body>
</html>
```